Business consultancy needs a greeting card (Thank you/gratitude) design

We need a Thank You card for a start up company located in Melbourne Australia. Part of the business is about learning to say thank you and being grateful so one of the products we will sell is a Thank you Card. We would like the design to be innovative, trendy, in line with our motto, "courage to make a difference" and business name/logo (Lantern Bloom which is about influencing others in a positive way which then continues to ripple on). By taking the effort of thanking people using a card is going the extra effort.
The design should include the Lantern Bloom colours (orange R250 g165 b65, blue R49 g 118 b192, purple r 183 g 165 b 210). Reference website: mylanternbloom.example Logo was uploaded but don't want part of the design, just as a reference. The card to be: trendy/make you feel happy. Would love some sort of "ripple".

Target Market(s)

Small businesses, individuals, younger generation

Industry/Entity Type

Business

• See logo. Use something trendy

Colors
876aae
f78f20
0555a3

Requirements
Must have
• trendy, creative, innovative. Use colours as seen in the project description. Add some sort of "ripple" (don't use water though)
Should not have
• Off the shelf type of look

```html
<!DOCTYPE html>
<html lang="en">
<head>
<meta charset="utf-8">
<title>Endless gratitude – thank you card</title>
<link rel="preconnect" href="https://fonts.googleapis.com">
<link href="https://fonts.googleapis.com/css2?family=Nanum+Pen+Script&display=swap" rel="stylesheet">
<style>
  :root {
    --lavender: #b9a7f5;
    --lavender-line: rgba(140, 150, 255, 0.28);
    --ripple-blue: #3380fb;
    --bloom-orange: #f7972c;
    --ink-white: #ffffff;
    --shadow: rgba(60, 40, 120, 0.45);
  }
  html, body {
    margin: 0;
    padding: 0;
    overflow: hidden;
    background: var(--lavender);
  }
  .card {
    position: relative;
    width: 1200px;
    height: 862px;
    overflow: hidden;
    background-color: var(--lavender);
    background-image: repeating-linear-gradient(
      to bottom,
      transparent 0,
      transparent 3px,
      var(--lavender-line) 3px,
      var(--lavender-line) 4px
    );
  }
  .ripples {
    position: absolute;
    inset: 0;
    width: 1200px;
    height: 862px;
  }
  .ripple-band {
    fill: var(--ripple-blue);
  }
  .flourish {
    position: absolute;
    left: 0;
    top: 0;
    width: 1200px;
    height: 862px;
  }
  .greeting {
    position: absolute;
    left: 210px;
    top: 118px;
    margin: 0;
    font-family: "Nanum Pen Script", cursive;
    font-weight: 400;
    font-size: 132px;
    line-height: 1;
    letter-spacing: 1px;
    color: var(--ink-white);
    text-shadow: 6px 8px 8px var(--shadow);
    white-space: nowrap;
  }
</style>
</head>
<body>
  <main class="card">
    <svg class="ripples" viewBox="0 0 1299 933" aria-hidden="true">
      <defs>
        <filter id="soft-edge" x="-5%" y="-5%" width="110%" height="110%">
          <feGaussianBlur stdDeviation="3"/>
        </filter>
      </defs>
      <path class="ripple-band" filter="url(#soft-edge)"
        d="M0,212 Q330,430 760,458 L1299,482 L1299,585 Q930,575 700,545 Q290,480 0,242 Z"/>
      <path class="ripple-band" filter="url(#soft-edge)"
        d="M0,418 Q320,575 820,650 Q1080,680 1299,690 L1299,872 Q850,840 520,775 Q200,710 0,690 Z"/>
    </svg>

    <svg class="flourish" viewBox="0 0 1299 933" role="img"
         aria-label="Large orange calligraphic flourish looping over the blue ripple bands">
      <defs>
        <radialGradient id="flourish-glow" cx="0.5" cy="0.5" r="0.5">
          <stop offset="0" stop-color="var(--bloom-orange)" stop-opacity="0.9"/>
          <stop offset="0.6" stop-color="var(--bloom-orange)" stop-opacity="0.55"/>
          <stop offset="1" stop-color="var(--bloom-orange)" stop-opacity="0"/>
        </radialGradient>
      </defs>
      <ellipse cx="380" cy="600" rx="380" ry="360" fill="url(#flourish-glow)"/>
    </svg>

    <h1 class="greeting">Endless gratitude!</h1>
  </main>
</body>
</html>
```